bright meadowline requires some business cards

I need some business cards created that feature the company's newly designed logo. The business cards need to be be double sided and be a standard Australian size of 90mm x 55mm

Target Market(s)

business professionals, company executives, local goverment

Industry/Entity Type

Business

Requirements
Must have
• Company's logo
• The information section must include
• Individual name:
• Position:
• Phone:
• Address:
• Email:
• Website: www.brightmeadowline.example
• The cards need to be easily formatted so I can enter staff members details positions etc...
• I plan to get these printed at deskhaven so can you please ensure that all designs meet their printing requirements http://www.deskhaven.example/retail/b2c/opsProductCreate.do?qty=1&cardQty=1000&sided=double&productname=colourbusinesscards&category=businesscards
Nice to have
• I might like to see some of the services we offer printed on one of the faces:
• Lighting Design (architectural, commercial, residential, theatrical ,exterior, interior) Lighting Consultancy, Theatrical Consultancy

```html
<!DOCTYPE html>
<html lang="en">
<head>
<meta charset="utf-8">
<title>bright meadowline — business cards</title>
<link rel="stylesheet" href="https://fonts.googleapis.com/css2?family=Arimo:wght@400&display=swap">
<style>
  :root {
    --stage: #e9e7e3;
    --card: #050505;
    --card-edge: #1a1a1a;
    --name-blue: #1c9ad8;
    --text-grey: #8a8a8a;
    --logo-grey: #c9c9c9;
    --glow-blue: #1d6fa8;
    --glow-violet: #6b3ea8;
    --glow-magenta: #b0407a;
    --glow-amber: #c0702a;
  }
  * { box-sizing: border-box; margin: 0; padding: 0; }
  html, body {
    width: 1200px; height: 755px; overflow: hidden;
    background: var(--stage);
    font-family: "Arimo", Arial, sans-serif;
  }
  .sheet {
    position: relative; width: 1200px; height: 755px;
    display: flex; align-items: center; justify-content: center; gap: 54px;
  }
  .card {
    position: relative; width: 520px; height: 318px;
    background: var(--card);
    border: 1px solid var(--card-edge);
    overflow: hidden;
    box-shadow: 0 10px 30px rgba(0,0,0,0.25);
  }
  .card__glow {
    position: absolute; inset: 0;
  }
  .card--back .card__glow {
    background:
      radial-gradient(ellipse 60% 22% at 55% 45%, rgba(255,255,255,0.08), transparent 70%),
      linear-gradient(165deg, transparent 28%,
        rgba(29,111,168,0.55) 40%, rgba(107,62,168,0.55) 50%,
        rgba(176,64,122,0.5) 60%, rgba(192,112,42,0.4) 68%, transparent 80%);
    opacity: 0.85;
  }
  .card--front .card__glow {
    background:
      linear-gradient(165deg, transparent 35%,
        rgba(29,111,168,0.25) 48%, rgba(107,62,168,0.22) 56%,
        rgba(176,64,122,0.22) 64%, rgba(192,112,42,0.18) 70%, transparent 82%);
  }
  .logo {
    position: absolute; left: 50%; top: 50%;
    transform: translate(-50%, -50%);
    display: flex; align-items: center; gap: 10px;
    color: var(--logo-grey);
    font-size: 24px; letter-spacing: 0.2px;
  }
  .logo__mark {
    width: 16px; height: 16px; border-radius: 50%;
    background: var(--logo-grey);
  }
  .person {
    position: absolute; right: 30px; top: 28px; text-align: right;
  }
  .person__name {
    color: var(--name-blue); font-size: 28px; font-weight: 400; line-height: 1.1;
  }
  .person__role {
    color: var(--text-grey); font-size: 12px; margin-top: 6px;
  }
  .contact {
    position: absolute; left: 30px; bottom: 26px;
    list-style: none; color: var(--text-grey);
    font-size: 13px; line-height: 1.75;
  }
</style>
</head>
<body>
<main class="sheet">
  <section class="card card--back" aria-label="Card back">
    <div class="card__glow" role="img" aria-label="Dotted light-spectrum pattern in blue, violet, magenta and amber"></div>
    <div class="logo">
      <span class="logo__mark"></span>
      <span class="logo__name">bright meadowline</span>
    </div>
  </section>

  <section class="card card--front" aria-label="Card front">
    <div class="card__glow" role="img" aria-label="Faint dotted light-spectrum pattern"></div>
    <header class="person">
      <h1 class="person__name">Marcus Vale</h1>
      <p class="person__role">Marketing director</p>
    </header>
    <ul class="contact">
      <li class="contact__phone">+61 8 9555 0142</li>
      <li class="contact__web">www.brightmeadowline.example</li>
      <li class="contact__email">marcus@brightmeadowline.example</li>
      <li class="contact__address">PO Box 000, Kestrel Bay WA 6999 Australia</li>
    </ul>
  </section>
</main>
</body>
</html>
```